Wealth management firm needs a business card design

Using my logo, create a business card that covers all of the regulatory wordings that I need. It must have - Registered Office 5-7 Pellinore Court, Edinburgh, EH9 2QW. Registered in Scotland under number SC738204. Corvell Wealth Management Ltd is an appointed representative of Quintor wealth management Ltd, which is authorised and regulated by the Monetary Standards Council.

Target Market(s)

professional clients

Industry/Entity Type

finance

Contact Information for Business Card

Corvell Wealth Management, Rupert Ashdown-Kerr, Director, 9 Tanner Row, Edinburgh, EH2 4NP. 07812 455 193, rupert.ashdown-kerr@corvellwealth.example , www.corvellwealth.example

Font styles to use
Serif

Colors
0054AA
0677BA
7BADD7
CADEEF
E8F1F8

Requirements
Must have
• regulatory wording in small text at bottom

```html
<!DOCTYPE html>
<html lang="en">
<head>
<meta charset="utf-8">
<title>Corvell Wealth Management – Business Card</title>
<link rel="stylesheet" href="https://fonts.googleapis.com/css2?family=Noto+Serif:wght@400;700&family=Montserrat:wght@400;500;600&display=swap">
<style>
  :root {
    --page-bg: #3b3b3b;
    --card-light: #ffffff;
    --card-dark: #262626;
    --brand-blue: #1a7ff0;
    --brand-deep: #0054aa;
    --ink: #1c1c1c;
    --ink-soft: #333333;
    --paper-text: #f2f2f2;
  }
  * { box-sizing: border-box; margin: 0; padding: 0; }
  html, body { width: 1200px; height: 1200px; overflow: hidden; }
  body {
    background: var(--page-bg);
    display: flex;
    flex-direction: column;
    align-items: center;
    justify-content: center;
    gap: 48px;
    font-family: "Montserrat", sans-serif;
  }
  .card {
    position: relative;
    width: 900px;
    height: 514px;
    border-radius: 36px;
    border-bottom: 5px solid var(--brand-blue);
    overflow: hidden;
  }
  .card--front { background: var(--card-light); color: var(--ink); }
  .card--back { background: var(--card-dark); color: var(--paper-text); }

  .brand {
    position: absolute;
    left: 0; right: 0;
    display: flex;
    flex-direction: column;
    align-items: center;
  }
  .brand__mark {
    width: 96px; height: 96px;
    border-radius: 50%;
    background: var(--brand-blue);
    margin-bottom: 22px;
  }
  .brand__name {
    font-family: "Noto Serif", serif;
    font-weight: 400;
    font-size: 42px;
    letter-spacing: 0.5px;
    line-height: 1;
  }
  .brand__tagline {
    font-family: "Noto Serif", serif;
    font-size: 16px;
    letter-spacing: 0.6px;
    margin-top: 8px;
  }
  .card--front .brand { top: 50px; }
  .card--front .brand__name { color: var(--ink); }
  .card--front .brand__tagline { color: var(--ink-soft); }
  .card--back .brand { top: 78px; }
  .card--back .brand__name { color: #ffffff; font-size: 50px; }
  .card--back .brand__tagline { color: #ffffff; font-size: 19px; }

  .person { position: absolute; left: 70px; top: 300px; }
  .person__name { color: var(--brand-blue); font-size: 36px; font-weight: 600; letter-spacing: -0.5px; }
  .person__role { font-size: 19px; letter-spacing: 0.5px; margin-top: 2px; }

  .divider {
    position: absolute;
    left: 70px; right: 70px; top: 378px;
    height: 2px;
    background: var(--brand-blue);
  }
  .contact {
    position: absolute;
    top: 398px;
    list-style: none;
    font-size: 16px;
    line-height: 1.75;
    white-space: nowrap;
  }
  .contact--personal { left: 70px; }
  .contact--office { left: 560px; }
  .contact li { display: flex; align-items: flex-start; gap: 12px; }
  .contact svg { width: 20px; height: 20px; flex: none; margin-top: 5px; fill: var(--brand-blue); }

  .regulatory {
    position: absolute;
    left: 60px; right: 60px; bottom: 44px;
    text-align: center;
    font-size: 14.5px;
    line-height: 1.5;
    color: #ffffff;
  }
  .regulatory p + p { margin-top: 6px; }
</style>
</head>
<body>

<section class="card card--front" aria-label="Business card front">
  <div class="brand">
    <div class="brand__mark"></div>
    <div class="brand__name">Corvell Wealth Management Ltd</div>
    <div class="brand__tagline">Personal Financial Advice</div>
  </div>

  <div class="person">
    <div class="person__name">Rupert Ashdown-Kerr</div>
    <div class="person__role">DIRECTOR</div>
  </div>

  <div class="divider"></div>

  <ul class="contact contact--personal">
    <li>
      <svg viewBox="0 0 24 24" aria-hidden="true"><path d="M6.6 10.8a15.2 15.2 0 0 0 6.6 6.6l2.2-2.2a1 1 0 0 1 1-.25 11.4 11.4 0 0 0 3.6.57 1 1 0 0 1 1 1V20a1 1 0 0 1-1 1A17 17 0 0 1 3 4a1 1 0 0 1 1-1h3.5a1 1 0 0 1 1 1c0 1.25.2 2.45.57 3.57a1 1 0 0 1-.25 1z"/></svg>
      <span>07812 455 193</span>
    </li>
    <li>
      <svg viewBox="0 0 24 24" aria-hidden="true"><path d="M2 5h20v14H2z M3.5 6.5 12 13l8.5-6.5" fill="none" stroke="#1a7ff0" stroke-width="2"/><path d="M2 5h20L12 12.5z"/></svg>
      <span>rupert.ashdown-kerr@corvellwealth.example</span>
    </li>
  </ul>

  <ul class="contact contact--office">
    <li>
      <svg viewBox="0 0 24 24" aria-hidden="true"><circle cx="12" cy="12" r="9" fill="none" stroke="#1a7ff0" stroke-width="2"/><path d="M3 12h18M12 3c3 3 3 15 0 18M12 3c-3 3-3 15 0 18M5 7.5h14M5 16.5h14" fill="none" stroke="#1a7ff0" stroke-width="1.5"/></svg>
      <span>www.corvellwealth.example</span>
    </li>
    <li>
      <svg viewBox="0 0 24 24" aria-hidden="true"><path d="M12 2a7 7 0 0 0-7 7c0 5 7 13 7 13s7-8 7-13a7 7 0 0 0-7-7zm0 9.5A2.5 2.5 0 1 1 12 6.5a2.5 2.5 0 0 1 0 5z"/></svg>
      <span>9 Tanner Row, Edinburgh,<br>EH2 4NP. 07812 455 193</span>
    </li>
  </ul>
</section>

<section class="card card--back" aria-label="Business card back">
  <div class="brand">
    <div class="brand__mark"></div>
    <div class="brand__name">Corvell Wealth Management Ltd</div>
    <div class="brand__tagline">Personal Financial Advice</div>
  </div>

  <div class="regulatory">
    <p>Registered Office 5-7 Pellinore Court, Edinburgh, EH9 2QW.<br>Registered in Scotland Number: SC738204</p>
    <p>Corvell Wealth Management Ltd is an appointed representative of Quintor wealth management Ltd,<br>which is authorised and regulated by the Monetary Standards Council.</p>
  </div>
</section>

</body>
</html>
```